Ferrowave.com website design

I need a basic website for www.ferrowave.com. Ferro Wave has been hosting websites since 2002 via partnership arrangement with Stackhollow.com and Namequarry.com. We do not do any design, only hosting for small companies and nonprofits. We are referring people to PixelGuild and others to get their websites developed. Our website and pricing does not change often, but I need to be able to easily update the pricing and contact page.

Target Market(s)

Small company and non profit organizations

Industry/Entity Type

Utility

Coding

Coded - Design and coding required

Number of Pages Required

5+ page

Colors

Designer to choose colors to be used in the design.

Requirements
Must have
• Wordsmith format for easy content management. The logo attached. Contact us page with the following: Phone and fax are the same number: 888.514.2973. Email address is myferrowave@mailnest.example. Mailing address is 4819 E. Tolliver Bend #317, Alder Falls, OK 74902.
Nice to have
• Some kind of badge or tag line on the home page that celebrates our 15th year of hosting without a single hosting without any downtime. We are are 15 year partners with Stackhollow.com and Namequarry.com. Website Design tab needs to reference PixelGuild or others for all their website design needs. We provide no design or updating services. We will provide the developers FTP access to our dedicated Linux server. We do not provide email services other than redirects to their proprietary email or gmail, yahoo, etc. Needs a services and pricing tab. We provide domain registration services via our partnership with Namequarry.com. We will want a way for them to submit a suggested domain name for us to verify if available. I might be able to get a link from Namequarry.com to our account for you to include on that tab REGISTER DOMAIN. The tab buttons can be: WHO WE ARE, WHAT WE DO, WHEN YOU NEED US, WHERE TO REACH US. Maybe consider making the WHO, WHAT, WHEN and WHERE a dark blue color the rest of the text different color just so they stand out
Should not have
• A lot of animation that takes a long time to open. Clean and simple website.

```html
<!DOCTYPE html>
<html lang="en">
<head>
<meta charset="utf-8">
<title>Ferro Wave — Unlimited Web Hosting</title>
<link rel="stylesheet" href="https://fonts.googleapis.com/css2?family=Roboto:wght@300;400;500;700&display=swap">
<style>
:root{
  --blue:#3b8fd4;
  --blue-dark:#2f7cc0;
  --navy:#13304d;
  --navy-deep:#0d2238;
  --ink:#222a33;
  --text:#5c6670;
  --muted:#8a939c;
  --orange:#e8832a;
  --grey-band:#ececec;
  --grey-circle:#e9edf0;
  --footer:#2c333c;
  --footer-bar:#20262d;
  --white:#ffffff;
}
*{box-sizing:border-box;margin:0;padding:0}
html,body{width:1200px;height:3689px;overflow:hidden}
body{font-family:'Roboto',Arial,sans-serif;color:var(--text);background:var(--white);position:relative}
section,header,footer{position:absolute;left:0;width:1200px;overflow:hidden}
.abs{position:absolute}
.center{left:0;width:1200px;text-align:center}

/* header + hero */
.hero{top:0;height:462px}
.hero-bg{position:absolute;inset:0;background:linear-gradient(100deg,#2c3c4c 0%,#3f5566 45%,#566b7a 70%,#3a4b5a 100%)}
.hero-person{position:absolute;left:740px;top:70px;width:250px;height:392px;background:linear-gradient(180deg,#7c8a96 0%,#2a2f36 55%,#1d2126 100%);border-radius:120px 120px 0 0;opacity:.85}
.nav{position:absolute;top:0;left:0;width:1200px;height:69px}
.brand{position:absolute;left:232px;top:20px;display:flex;align-items:center;gap:10px;color:var(--white);font-weight:700;font-size:18px;letter-spacing:.5px}
.brand-square{width:28px;height:28px;background:var(--blue)}
.menu{position:absolute;left:500px;top:28px;display:flex;gap:26px;font-size:11px;font-weight:500;color:var(--white);letter-spacing:.4px}
.menu .active{color:var(--blue)}
.hero-kicker{left:246px;top:152px;font-size:19px;font-weight:300;color:#dfe6ec;letter-spacing:.5px}
.hero-line1{left:244px;top:176px;font-size:46px;font-weight:300;color:var(--white);line-height:1}
.hero-line2{left:244px;top:224px;font-size:46px;font-weight:700;color:var(--white);line-height:1}
.hero-price{left:246px;top:290px;display:flex;align-items:center;gap:8px;color:var(--white)}
.hero-price small{font-size:11px;line-height:1.1;color:#dfe6ec}
.hero-price strong{font-size:28px;font-weight:500}
.hero-price span{font-size:12px;color:#dfe6ec}
.save-badge{left:422px;top:272px;width:66px;height:66px;border-radius:50%;background:var(--blue);color:var(--white);text-align:center;font-size:10px;line-height:1.1;padding-top:12px;border:2px solid rgba(255,255,255,.6)}
.save-badge b{display:block;font-size:18px}
.btn-ghost{top:357px;height:32px;border:1px solid var(--white);color:var(--white);font-size:11px;font-weight:500;line-height:30px;text-align:center;letter-spacing:.4px}

/* steps */
.steps{top:462px;height:453px;background:var(--white)}
.section-title{font-size:23px;font-weight:700;color:var(--ink);letter-spacing:.5px}
.step{top:120px;width:200px;text-align:center}
.step-icon{width:88px;height:88px;border-radius:50%;background:var(--blue);margin:0 auto;display:flex;align-items:center;justify-content:center;box-shadow:0 0 0 6px #e3eef8}
.step h3{margin-top:30px;font-size:16px;font-weight:700;color:var(--ink)}
.step p{margin-top:6px;font-size:11px;line-height:1.6;color:var(--muted)}
.starts{top:332px;font-size:13px;color:var(--muted)}
.price-pill{left:516px;top:364px;width:165px;height:40px;background:var(--blue);color:var(--white);display:flex;align-items:center;justify-content:center;gap:6px}
.price-pill small{font-size:9px;line-height:1}
.price-pill strong{font-size:28px;font-weight:700}
.price-pill span{font-size:11px}

/* domain */
.domain{top:915px;height:241px;background:linear-gradient(120deg,var(--navy-deep),var(--navy) 50%,var(--navy-deep))}
.domain-title{top:72px;font-size:22px;font-weight:700;color:var(--white)}
.domain-sub{top:102px;font-size:12px;color:#c5d3e0}
.domain-input{left:337px;top:137px;width:400px;height:35px;background:var(--white);font-size:11px;color:var(--muted);line-height:35px;padding-left:12px}
.domain-btn{left:743px;top:137px;width:125px;height:35px;background:var(--blue);color:var(--white);font-size:12px;font-weight:500;line-height:35px;text-align:center}

/* packages */
.plans-head{top:1156px;height:182px;background:var(--white)}
.plan{left:0;width:1200px;height:345px}
.plan-std{top:1272px;background:var(--white)}
.plan-res{top:1611px;height:339px;background:var(--grey-band)}
.plan-unl{top:1950px;height:349px;background:var(--white)}
.plan-title{font-size:29px;color:var(--ink);font-weight:700;letter-spacing:.3px}
.plan-title span{font-weight:300;color:#7a838c}
.plan-desc{font-size:17px;line-height:1.45;color:#6a737c;width:375px}
.plan-feats{font-size:10px;color:var(--muted);width:360px;line-height:1.9}
.plan-price{font-size:18px;color:#7a838c;font-weight:400}
.plan-price b{font-size:30px;color:var(--orange);font-weight:700}
.btn-outline{width:116px;height:35px;border:1px solid #555;color:var(--ink);font-size:11px;font-weight:700;text-align:center;line-height:33px}
.illus{width:246px;height:246px;border-radius:50%}
.right-align{text-align:right}

/* features */
.why{top:2299px;height:529px;background:var(--blue)}
.why-title{top:56px;font-size:22px;font-weight:700;color:var(--white)}
.why-sub{top:84px;font-size:11px;font-weight:700;color:var(--white);letter-spacing:.3px}
.feature{width:170px;color:var(--white)}
.feature h4{margin-top:10px;font-size:12px;font-weight:500}
.feature hr{border:0;border-top:1px solid rgba(255,255,255,.6);width:32px;margin:6px 0 8px}
.feature p{font-size:10px;line-height:1.6;color:#e2eef9}
.why-btn{left:521px;top:440px;width:158px;height:34px;background:var(--white);color:var(--ink);font-size:11px;font-weight:500;line-height:34px;text-align:center}

/* featured services */
.featured{top:2828px;height:450px}
.featured-bg{position:absolute;inset:0;background:linear-gradient(180deg,#c9cdd1 0%,#e4e6e8 60%,#dadde0 100%)}
.featured-title{top:56px;font-size:22px;font-weight:700;color:var(--ink)}
.card{left:320px;top:108px;width:560px;height:273px;background:var(--white);box-shadow:0 2px 6px rgba(0,0,0,.08)}
.card-tab{left:196px;top:0;width:160px;height:40px;background:var(--blue);color:var(--white);font-size:15px;letter-spacing:.5px;line-height:40px;text-align:center}
.card-img{left:24px;top:79px;width:202px;height:128px;background:linear-gradient(135deg,#8fb6d8,#3f6f9b)}
.card-title{left:246px;top:80px;width:290px;font-size:16px;font-weight:700;color:var(--ink);line-height:1.3}
.card-body{left:246px;top:130px;width:290px;font-size:10px;color:var(--muted);line-height:1.55}
.card-btn{left:246px;top:192px;width:88px;height:27px;border:1px solid var(--blue);color:var(--ink);font-size:9px;font-weight:500;line-height:25px;text-align:center}
.slider-arrow{top:236px}

/* support */
.support{top:3278px;height:91px;background:var(--white)}
.support p{position:absolute;left:0;width:1200px;text-align:center;top:36px;font-size:14px;color:#4a525a;letter-spacing:.2px}
.support b{color:var(--ink)}

/* footer */
.footer{top:3369px;height:265px;background:var(--footer)}
.foot-brand{left:266px;top:64px;display:flex;align-items:center;gap:8px;color:var(--white);font-weight:700;font-size:14px}
.foot-brand i{width:22px;height:22px;background:var(--white);display:block}
.foot-address{left:266px;top:110px;width:145px;font-size:9.5px;line-height:1.75;color:#b7bec6}
.foot-col{top:60px;width:170px}
.foot-col h5{font-size:12px;font-weight:700;color:var(--white);margin-bottom:10px}
.foot-col li{list-style:none;font-size:10px;line-height:1.78;color:#b7bec6}
.foot-bar{top:3634px;height:55px;background:var(--footer-bar)}
.copyright{left:234px;top:21px;font-size:9px;color:#8d959e}
.socials{left:846px;top:17px;display:flex;gap:8px}
.socials i{width:18px;height:18px;border-radius:50%;background:var(--blue);display:block}
</style>
</head>
<body>

<header class="hero">
  <div class="hero-bg" role="img" aria-label="Blurred office and city backdrop in dark blue-grey tones"></div>
  <div class="hero-person" role="img" aria-label="Smiling businessman in a dark suit with arms crossed"></div>
  <nav class="nav">
    <div class="brand"><span class="brand-square"></span>Ferro Wave</div>
    <div class="menu">
      <span class="active">HOME</span><span>WEB HOSTING</span><span>DOMAINS</span><span>FEATURES</span><span>SERVICES</span><span>SUPPORT</span><span>CONTACT</span>
      <svg width="12" height="12" viewBox="0 0 12 12"><circle cx="5" cy="5" r="3.8" fill="none" stroke="#fff" stroke-width="1.4"/><line x1="8" y1="8" x2="11" y2="11" stroke="#fff" stroke-width="1.4"/></svg>
    </div>
  </nav>
  <div class="abs hero-kicker">UNLIMITED WEB HOSTING</div>
  <div class="abs hero-line1">ALL YOU NEEDS</div>
  <div class="abs hero-line2">IN ONE PACKAGE</div>
  <div class="abs hero-price"><small>Starting<br>From</small><strong>$1.75</strong><span>/mo &rsaquo;</span></div>
  <div class="abs save-badge">Save<b>40%</b>NOW!</div>
  <div class="abs btn-ghost" style="left:246px;width:88px">VIEW PLANS</div>
  <div class="abs btn-ghost" style="left:344px;width:88px">SIGN UP NOW</div>
</header>

<section class="steps">
  <h2 class="abs center section-title" style="top:60px">HOW TO START YOUR WEBSITE ?</h2>
  <svg class="abs" style="left:250px;top:100px" width="700" height="100" viewBox="0 0 700 100">
    <path d="M0 70 Q170 40 345 68 T690 20" fill="none" stroke="#cfd6dc" stroke-width="1.5" stroke-dasharray="5 5"/>
    <path d="M680 16 L695 18 L684 28" fill="none" stroke="var(--blue)" stroke-width="2"/>
    <g stroke="#b8c0c8" stroke-width="1.5"><line x1="240" y1="44" x2="250" y2="44"/><line x1="245" y1="39" x2="245" y2="49"/><line x1="446" y1="66" x2="456" y2="66"/><line x1="451" y1="61" x2="451" y2="71"/></g>
  </svg>
  <div class="abs step" style="left:289px">
    <div class="step-icon"><svg width="46" height="20" viewBox="0 0 46 20"><rect x="1" y="1" width="44" height="18" rx="3" fill="none" stroke="#fff" stroke-width="2"/><text x="23" y="14" font-size="9" fill="#fff" text-anchor="middle" font-family="Roboto,Arial,sans-serif">www.</text></svg></div>
    <h3>Domain</h3><p>Many web sites still in their versions<br>have evolved over the years.</p>
  </div>
  <div class="abs step" style="left:495px">
    <div class="step-icon"><svg width="36" height="36" viewBox="0 0 36 36" fill="none" stroke="#fff" stroke-width="2"><rect x="3" y="3" width="30" height="8" rx="1"/><rect x="3" y="14" width="30" height="8" rx="1"/><rect x="3" y="25" width="30" height="8" rx="1"/></svg></div>
    <h3>Hosting</h3><p>Many web sites still in their versions<br>have evolved over the years.</p>
  </div>
  <div class="abs step" style="left:700px">
    <div class="step-icon"><svg width="38" height="30" viewBox="0 0 38 30" fill="none" stroke="#fff" stroke-width="2"><rect x="1" y="1" width="36" height="28" rx="2"/><line x1="1" y1="8" x2="37" y2="8"/><rect x="7" y="13" width="12" height="10"/></svg></div>
    <h3>WebSite</h3><p>Many web sites still in their versions<br>have evolved over the years.</p>
  </div>
  <div class="abs center starts">All Starts form Just</div>
  <div class="abs price-pill"><small>only</small><strong>$1.75</strong><span>/mo</span></div>
</section>

<section class="domain">
  <h2 class="abs center domain-title">FIND YOUR PERFECT DOMAIN</h2>
  <div class="abs center domain-sub">Starting from $1.99 per year!</div>
  <div class="abs domain-input">Enter your domain name here...</div>
  <div class="abs domain-btn">SEARCH DOMAIN</div>
</section>

<section class="plans-head">
  <h2 class="abs center section-title" style="top:70px">CHOOSE PERFECT PACKAGE FOR YOU</h2>
  <div class="abs center" style="top:101px;font-size:10px;color:var(--muted)">Ferro Wave providing best and cheap web hosting packages</div>
</section>

<section class="plan plan-std">
  <h3 class="abs plan-title" style="left:270px;top:50px">STANDARD <span>HOSTING</span></h3>
  <p class="abs plan-desc" style="left:270px;top:98px">Many web sites still in infancy various have versions evolved over the years.</p>
  <p class="abs plan-feats" style="left:270px;top:154px">· Free Domain name &nbsp;· Unlimited Web Space &nbsp;· Free SSL Certificate<br>· Unlimited FTP Accounts &nbsp;· Unlimited Sub Domains</p>
  <div class="abs plan-price" style="left:270px;top:204px">STARTING AT JUST <b>$1.75</b>/MO</div>
  <div class="abs btn-outline" style="left:270px;top:258px">BUY NOW</div>
  <div class="abs illus" style="left:681px;top:56px;background:var(--grey-circle)" role="img" aria-label="Flat monitor showing a blank web page"></div>
</section>

<section class="plan plan-res">
  <div class="abs illus" style="left:270px;top:41px;background:var(--white)" role="img" aria-label="Flat monitor showing a handshake on an orange screen"></div>
  <h3 class="abs plan-title right-align" style="left:530px;width:400px;top:46px">RESELLER <span>HOSTING</span></h3>
  <p class="abs plan-desc right-align" style="left:555px;top:94px">Many web sites still in infancy various have versions evolved over the years.</p>
  <p class="abs plan-feats right-align" style="left:570px;top:150px">· Free Domain name &nbsp;· Unlimited Web Space &nbsp;· Free SSL Certificate<br>· Unlimited FTP Accounts &nbsp;· Unlimited Sub Domains</p>
  <div class="abs plan-price right-align" style="left:530px;width:400px;top:204px">STARTING AT JUST <b>$27</b>/MO</div>
  <div class="abs btn-outline" style="left:814px;top:253px">BUY NOW</div>
</section>

<section class="plan plan-unl">
  <h3 class="abs plan-title" style="left:270px;top:52px">UNLIMITED <span>HOSTING</span></h3>
  <p class="abs plan-desc" style="left:270px;top:100px">Many web sites still in infancy various have versions evolved over the years.</p>
  <p class="abs plan-feats" style="left:270px;top:156px">· Free Domain name &nbsp;· Unlimited Web Space &nbsp;· Free SSL Certificate<br>· Unlimited FTP Accounts &nbsp;· Unlimited Sub Domains</p>
  <div class="abs plan-price" style="left:270px;top:208px">STARTING AT JUST <b>$4.95</b>/MO</div>
  <div class="abs btn-outline" style="left:270px;top:261px">BUY NOW</div>
  <div class="abs illus" style="left:681px;top:42px;background:var(--grey-circle)" role="img" aria-label="Flat monitor with orange domain extension boxes on a green screen"></div>
</section>

<section class="why">
  <h2 class="abs center why-title">WHY CHOOSE OUR WEB HOSTING?</h2>
  <div class="abs center why-sub">MORE THAN 200,000 WEBSITES HOSTED</div>

  <div class="abs feature" style="left:234px;top:180px"><svg width="18" height="16" viewBox="0 0 18 16" fill="none" stroke="#fff" stroke-width="1.5"><path d="M1 8 A8 7 0 0 1 17 8 Z"/><path d="M9 8 V14 a1.5 1.5 0 0 1 -3 0"/></svg><h4>99.9% Uptime Guarantee</h4><hr><p>Desktop publishing packages web page model and a for many web sites.</p></div>
  <div class="abs feature" style="left:418px;top:180px"><svg width="18" height="16" viewBox="0 0 18 16" fill="none" stroke="#fff" stroke-width="1.5"><path d="M1 7 L17 1 L12 15 L8 9 Z"/><path d="M8 9 L17 1"/></svg><h4>One FREE Domain for Life</h4><hr><p>Desktop publishing packages web page model and a for many web sites.</p></div>
  <div class="abs feature" style="left:602px;top:180px"><svg width="18" height="16" viewBox="0 0 18 16" fill="none" stroke="#fff" stroke-width="1.5"><path d="M1 8 A8 7 0 0 1 17 8 Z"/><path d="M9 8 V14 a1.5 1.5 0 0 1 -3 0"/></svg><h4>Unlimited Disk Space</h4><hr><p>Desktop publishing packages web page model and a for many web sites.</p></div>
  <div class="abs feature" style="left:792px;top:180px"><svg width="18" height="16" viewBox="0 0 18 16" fill="none" stroke="#fff" stroke-width="1.5"><path d="M1 7 L17 1 L12 15 L8 9 Z"/><path d="M8 9 L17 1"/></svg><h4>Advanced Security Scan</h4><hr><p>Desktop publishing packages web page model and a for many web sites.</p></div>

  <div class="abs feature" style="left:234px;top:332px"><svg width="18" height="16" viewBox="0 0 18 16" fill="none" stroke="#fff" stroke-width="1.5"><path d="M1 8 A8 7 0 0 1 17 8 Z"/><path d="M9 8 V14 a1.5 1.5 0 0 1 -3 0"/></svg><h4>Host Unlimited Domains</h4><hr><p>Desktop publishing packages web page model and a for many web sites.</p></div>
  <div class="abs feature" style="left:418px;top:332px"><svg width="18" height="16" viewBox="0 0 18 16" fill="none" stroke="#fff" stroke-width="1.5"><path d="M1 7 L17 1 L12 15 L8 9 Z"/><path d="M8 9 L17 1"/></svg><h4>Free 24/7/365 Support</h4><hr><p>Desktop publishing packages web page model and a for many web sites.</p></div>
  <div class="abs feature" style="left:602px;top:332px"><svg width="18" height="16" viewBox="0 0 18 16" fill="none" stroke="#fff" stroke-width="1.5"><path d="M1 8 A8 7 0 0 1 17 8 Z"/><path d="M9 8 V14 a1.5 1.5 0 0 1 -3 0"/></svg><h4>EasyDesk Control Panel</h4><hr><p>Desktop publishing packages web page model and a for many web sites.</p></div>
  <div class="abs feature" style="left:792px;top:332px"><svg width="18" height="16" viewBox="0 0 18 16" fill="none" stroke="#fff" stroke-width="1.5"><path d="M1 7 L17 1 L12 15 L8 9 Z"/><path d="M8 9 L17 1"/></svg><h4>30 Day Money-back Guarantee</h4><hr><p>Desktop publishing packages web page model and a for many web sites.</p></div>

  <div class="abs why-btn">VIEW ALL FEATURES</div>
</section>

<section class="featured">
  <div class="featured-bg" role="img" aria-label="Faint photo of a modern glass office building"></div>
  <h2 class="abs center featured-title">FEATURED SERVICES</h2>
  <svg class="abs slider-arrow" style="left:286px" width="14" height="26" viewBox="0 0 14 26"><path d="M12 2 L2 13 L12 24" fill="none" stroke="#555" stroke-width="2"/></svg>
  <svg class="abs slider-arrow" style="left:900px" width="14" height="26" viewBox="0 0 14 26"><path d="M2 2 L12 13 L2 24" fill="none" stroke="#555" stroke-width="2"/></svg>
  <div class="abs card">
    <div class="abs card-tab">WEB HOSTING</div>
    <div class="abs card-img" role="img" aria-label="Hand touching a glowing web hosting interface"></div>
    <div class="abs card-title">Providing quality web hosting with unlimited resources.</div>
    <div class="abs card-body">Lorem Ipsum as their default model text a search ipsum many web sites still in their infancy also the into electronic essentially was in sheets versions over the years.</div>
    <div class="abs card-btn">LEARN MORE</div>
  </div>
</section>

<section class="support">
  <p>NEED HELP? CALL OUR SUPPORT 24/7 AT <b>888.514.2973</b> OR myferrowave@mailnest.example</p>
</section>

<footer class="footer">
  <div class="abs foot-brand"><i></i>FERRO WAVE</div>
  <div class="abs foot-address">4819 E. Tolliver Bend #317,<br>Alder Falls, OK 74902<br><br>Phone or Fax: 888.514.2973<br>Email:<br>myferrowave@mailnest.example<br>View Directions</div>
  <div class="abs foot-col" style="left:423px"><h5>Hosting Packages</h5><ul><li>Web Hosting</li><li>Reseller Hosting</li><li>VPS Hosting</li><li>Dedicated Servers</li><li>Windows Hosting</li><li>Cloud Hosting</li><li>Linux Servers</li></ul></div>
  <div class="abs foot-col" style="left:612px"><h5>Our Products</h5><ul><li>Website Builder</li><li>Web Design</li><li>Logo Design</li><li>Register Domains</li><li>Traffic Booster</li><li>Search Advertising</li><li>Email Marketing</li></ul></div>
  <div class="abs foot-col" style="left:802px"><h5>Company</h5><ul><li>About Us</li><li>News / Blogs</li><li>Affiliate Program</li><li>Product Support</li><li>Contact Us</li><li>Knowledge Base</li><li>Tutorials</li></ul></div>
</footer>
<footer class="foot-bar">
  <div class="abs copyright">Copyright © 2017 Ferrowave.com. All rights reserved. Terms of Service | Privacy Policy</div>
  <div class="abs socials"><i></i><i></i><i></i><i></i><i></i></div>
</footer>

</body>
</html>
```